Brisk Meadow Home Page (A Home Wellness e-commerce site & blog)

We need a dynamic home page created for a home wellness brand. Must be visually appealing and extremely mobile-friendly. Logos and a Navmap have been provided but that is just a guideline, PLEASE USE YOUR CREATIVITY.

Target Market(s)

1st target demo: females 24-48, 2nd target demo: all 24-48

Number of Pages Required

1 page

```html
<!DOCTYPE html>
<html lang="en">
<head>
<meta charset="utf-8">
<title>Brisk Meadow — Home Wellness</title>
<link href="https://fonts.googleapis.com/css2?family=Montserrat:wght@500;600;700;800&family=Raleway:wght@400;500;600&display=swap" rel="stylesheet">
<style>
:root{
  --teal:#33bfc9;
  --purple:#5a2d91;
  --purple-deep:#4e2689;
  --ink:#1d1d1d;
  --grey:#777;
  --footer:#222222;
  --white:#fff;
}
*{margin:0;padding:0;box-sizing:border-box}
html,body{width:1200px;height:3735px;overflow:hidden}
body{position:relative;font-family:"Raleway",sans-serif;color:var(--ink);background:var(--white)}
.abs{position:absolute}

/* top bar */
.topbar{left:0;top:0;width:1200px;height:51px;background:var(--teal)}
.topbar-note{left:0;width:1200px;top:17px;text-align:center;color:#fff;font:700 13px "Montserrat",sans-serif}
.social-dots{display:flex;gap:8px}
.social-dots span{width:32px;height:32px;border-radius:50%;background:#fff;display:block}
.topbar .social-dots{position:absolute;left:932px;top:9px}

/* nav */
.nav{left:0;top:51px;width:1200px;height:117px;background:var(--purple)}
.brand{left:112px;top:40px;color:#fff;font:700 30px "Montserrat",sans-serif;letter-spacing:-0.5px}
.menu{left:397px;top:52px;display:flex;gap:33px;font:700 15px "Montserrat",sans-serif;color:#fff}
.menu .active{color:var(--teal);position:relative}
.menu .active::after{content:"";position:absolute;left:2px;top:22px;width:40px;height:12px;border-bottom:4px solid var(--teal);border-radius:0 0 30px 30px}
.cart{left:951px;top:40px;display:flex;align-items:center;gap:10px;color:#fff;font:700 15px "Montserrat",sans-serif}
.cart-icon{width:48px;height:48px;border-radius:50%;background:var(--teal);display:flex;align-items:center;justify-content:center}

/* hero */
.hero{left:0;top:168px;width:1200px;height:594px;background:linear-gradient(100deg,#d9cab7 0%,#cdbba6 45%,#e9e3da 62%,#c7a783 80%,#efe9df 100%)}
.hero-title{left:112px;top:332px;color:var(--purple);font:800 54px/54px "Montserrat",sans-serif}
.btn{display:inline-block;border-radius:24px;font:700 15px "Montserrat",sans-serif;text-align:center}
.btn-teal{background:var(--teal);color:#fff}
.btn-white{background:#fff;color:var(--ink)}
.hero-btn{left:113px;top:456px;width:138px;height:46px;line-height:46px}
.dots{left:114px;top:681px;display:flex;gap:5px}
.dots span{width:33px;height:33px;border-radius:50%;background:#fff;font:700 13px/33px "Montserrat",sans-serif;text-align:center}
.dots .on{background:var(--teal);color:#fff}

/* sale */
.sale{left:0;top:762px}
.sale-title{left:100px;top:850px;width:1000px;text-align:center;color:#fff;font:700 35px/43px "Montserrat",sans-serif}
.sale-btn{left:531px;top:966px;width:138px;height:47px;line-height:47px}

/* featured */
.section-title{width:1200px;left:0;text-align:center;font:700 35px "Montserrat",sans-serif;color:var(--ink)}
.tile{position:absolute;display:flex;align-items:flex-end;justify-content:center;padding-bottom:30px;color:#fff;font:700 18px/26px "Montserrat",sans-serif;text-align:center}
.plus{position:absolute;left:50%;top:50%;width:50px;height:50px;margin:-25px 0 0 -25px}

/* about */
.about-text{left:600px;color:#fff}
.about-title{top:1933px;font:700 35px "Montserrat",sans-serif}
.about-body{top:1994px;width:485px;font:500 14.5px/22px "Raleway",sans-serif}
.about-btn{left:596px;top:2123px;width:138px;height:46px;line-height:46px}
.photo-slot{background:rgba(255,255,255,0.18)}

/* pay later */
.paylater{left:0;top:2310px;width:1200px;height:369px;background:var(--purple-deep)}
.pl-brand{left:0;width:1200px;top:2410px;text-align:center;color:#fff;font:600 34px "Montserrat",sans-serif}
.pl-brand i{display:inline-block;width:30px;height:30px;border-radius:50%;background:#fff;vertical-align:-3px;margin-right:8px}
.pl-title{left:0;width:1200px;top:2456px;text-align:center;color:#fff;font:700 35px "Montserrat",sans-serif}
.pl-body{left:210px;width:780px;top:2515px;text-align:center;color:#fff;font:500 14.5px/22px "Raleway",sans-serif}

/* blog */
.blog-sub{left:0;width:1200px;top:2828px;text-align:center;font:500 14px "Raleway",sans-serif;color:var(--grey)}
.card{position:absolute;top:2878px;width:312px;text-align:center}
.card-img{height:213px;border-radius:18px 18px 0 0}
.card h3{margin-top:16px;font:700 18px/22px "Montserrat",sans-serif}
.card p{margin-top:12px;font:500 14.5px/22px "Raleway",sans-serif;color:var(--grey);padding:0 8px}
.card a{display:inline-block;margin-top:14px;font:700 14px "Montserrat",sans-serif;color:var(--purple);text-decoration:underline}
.arrow{width:44px;height:44px;border-radius:50%;display:flex;align-items:center;justify-content:center}
.chat{left:1097px;top:3322px;width:74px;height:74px;border-radius:50%;background:var(--teal);display:flex;align-items:center;justify-content:center;z-index:5}

/* footer */
.footer{left:0;top:3359px;width:1200px;height:376px;background:var(--footer)}
.f-brand{left:112px;top:3480px;color:#fff;font:700 26px "Montserrat",sans-serif}
.footer .social-dots{position:absolute;left:111px;top:208px;gap:7px}
.footer .social-dots span{width:34px;height:34px}
.f-col{top:3446px;color:#fff}
.f-col h4{font:700 17px "Montserrat",sans-serif;margin-bottom:16px}
.f-col li{list-style:none;font:500 13px/22px "Raleway",sans-serif;color:#bbb}
.f-col li::before{content:"»";margin-right:9px}
.f-col p{font:500 13px/22px "Raleway",sans-serif;color:#bbb;width:275px}
.email{left:815px;top:3554px;width:273px;height:45px;background:#333;color:#999;font:500 13px/45px "Raleway",sans-serif;padding-left:17px}
.copy{left:0;width:1200px;top:3681px;text-align:center;color:#fff;font:500 13px "Raleway",sans-serif}
</style>
</head>
<body>

<header>
  <div class="abs topbar">
    <div class="abs topbar-note">Free shipping on all orders $50 and over!</div>
    <div class="social-dots"><span></span><span></span><span></span><span></span></div>
  </div>
  <nav class="abs nav">
    <div class="abs brand">Brisk Meadow</div>
    <div class="abs menu">
      <span class="active">Home</span><span>About us</span><span>Services</span><span>Product</span><span>Blog</span><span>Contact us</span>
    </div>
    <div class="abs cart">
      <span class="cart-icon"><svg width="18" height="16" viewBox="0 0 18 16"><path d="M1 1h3l2 9h9l2-7H5" fill="none" stroke="#fff" stroke-width="2"/><circle cx="7" cy="14" r="1.6" fill="#fff"/><circle cx="14" cy="14" r="1.6" fill="#fff"/></svg></span>
      Cart $0.00
    </div>
  </nav>
</header>

<section>
  <div class="abs hero" role="img" aria-label="Spa still life with candles, bowls of cream and bath salt, a wooden brush and a palm leaf"></div>
  <svg class="abs" style="left:96px;top:260px" width="230" height="70" viewBox="0 0 230 70"><path d="M4 62 Q115 -30 222 62" fill="none" stroke="var(--teal)" stroke-width="26"/></svg>
  <h1 class="abs hero-title">We are a Home<br>Wellness company</h1>
  <span class="abs btn btn-teal hero-btn">Shop now</span>
  <div class="abs dots"><span class="on">1</span><span>2</span><span>3</span></div>
</section>

<section>
  <svg class="abs sale" width="1200" height="346" viewBox="0 0 1200 346"><path d="M0 0H1200V260Q600 430 0 260Z" fill="var(--teal)"/></svg>
  <h2 class="abs sale-title">50% off sale going on now! Because saving money alsomakes us happy</h2>
  <span class="abs btn btn-white sale-btn">Learn more</span>
</section>

<section>
  <h2 class="abs section-title" style="top:1190px">Featured Product</h2>
  <div class="tile" role="img" aria-label="Bath towels, soap and cream jar" style="left:112px;top:1268px;width:314px;height:200px;background:linear-gradient(#ddd6cf,#6e6964)">Lorem ipsum dolor sit amet consectetur</div>
  <div class="tile" role="img" aria-label="Oil bottle with a white flower on stone" style="left:442px;top:1268px;width:314px;height:414px;background:linear-gradient(160deg,#7b8597,#5b6476 60%,#4f6a3a)">
    <svg class="plus" viewBox="0 0 50 50"><path d="M25 0V50M0 25H50" stroke="#fff" stroke-width="2"/></svg>
  </div>
  <div class="tile" role="img" aria-label="Hands holding handmade soap with honey" style="left:772px;top:1268px;width:316px;height:200px;background:linear-gradient(#d3cbc0,#7c7267)">Lorem ipsum dolor sit amet consectetur</div>
  <div class="tile" role="img" aria-label="Skincare bottles on a shelf" style="left:112px;top:1481px;width:314px;height:201px;background:linear-gradient(#e8e2da,#6b645d)">Lorem ipsum dolor sit amet consectetur</div>
  <div class="tile" role="img" aria-label="White orchid and candles" style="left:772px;top:1481px;width:316px;height:201px;background:linear-gradient(#eeedf0,#777680)">Lorem ipsum dolor sit amet consectetur</div>
</section>

<section>
  <svg class="abs" style="left:0;top:1778px" width="1200" height="532" viewBox="0 0 1200 532"><path d="M0 82Q600 -80 1200 82V532H0Z" fill="var(--teal)"/></svg>
  <div class="abs photo-slot" role="img" aria-label="Placeholder: candle and bath salt on a wooden slice" style="left:18px;top:1980px;width:150px;height:265px"></div>
  <svg class="abs" style="left:145px;top:1850px" width="210" height="414" viewBox="0 0 210 414"><path d="M207 3A204 204 0 0 0 207 411" fill="none" stroke="var(--purple)" stroke-width="16"/></svg>
  <div class="abs" role="img" aria-label="Family sharing glasses of water on a sofa" style="left:160px;top:1866px;width:383px;height:383px;border-radius:50%;background:linear-gradient(135deg,#c9c1b6,#8c8378 60%,#5d6a80)"></div>
  <div class="abs photo-slot" role="img" aria-label="Placeholder: green leaves" style="left:918px;top:2080px;width:282px;height:230px"></div>
  <h2 class="abs about-text about-title">ABOUT US</h2>
  <p class="abs about-text about-body">They say that home is where the heart is. But home is also where your mind and body reside. At Brisk Meadow we believe that home should be your place of Zen. A respite from the crazy world outside those walls. It is where you recharge your soul so you can approach each day with the focus and energy necessary to conquer the world.</p>
  <span class="abs btn btn-white about-btn">Tell Me More</span>
</section>

<section>
  <div class="abs paylater"></div>
  <div class="abs pl-brand"><i></i>Tallyway</div>
  <h2 class="abs pl-title">Don’t sweat it. You can pay later.</h2>
  <p class="abs pl-body">Lorem ipsum dolor sit amet, consectetur adipiscing elit, sed do eiusmod tempor incididunt ut labore et dolore magna aliqua. Ut enim ad minim veniam, quis nostrud exercitation ullamco laboris nisi ut aliquip ex ea commodo consequat. Duis aute irure dolor in reprehenderit</p>
</section>

<section>
  <h2 class="abs section-title" style="top:2768px">The Happy Blog</h2>
  <p class="abs blog-sub">Food for the mind, tips for the body and exercises for the soul</p>
  <article class="card" style="left:112px">
    <div class="card-img" role="img" aria-label="Smiling couple at home" style="background:linear-gradient(#e5ded6,#b99b84)"></div>
    <h3>Lorem ipsum dolor sit amet, consectetur</h3>
    <p>Lorem ipsum dolor sit amet, consectetur adipiscing elit, sed do eiusmod tempor incididunt ut labore et dolo</p>
    <a>Learn more ➔</a>
  </article>
  <article class="card" style="left:443px">
    <div class="card-img" role="img" aria-label="Woman with towel at a mirror" style="background:linear-gradient(#ece6df,#c6ab95)"></div>
    <h3>Lorem ipsum dolor sit amet, consectetur</h3>
    <p>Lorem ipsum dolor sit amet, consectetur adipiscing elit, sed do eiusmod tempor incididunt ut labore et dolo</p>
    <a>Learn more ➔</a>
  </article>
  <article class="card" style="left:776px">
    <div class="card-img" role="img" aria-label="Woman meditating at home" style="background:linear-gradient(#d5d3cf,#6e6b66)"></div>
    <h3>Lorem ipsum dolor sit amet, consectetur</h3>
    <p>Lorem ipsum dolor sit amet, consectetur adipiscing elit, sed do eiusmod tempor incididunt ut labore et dolo</p>
    <a>Learn more ➔</a>
  </article>
  <div class="abs arrow" style="left:33px;top:3069px;background:#e6e6e6"><svg width="10" height="14"><path d="M8 1L2 7L8 13" fill="none" stroke="#333" stroke-width="1.6"/></svg></div>
  <div class="abs arrow" style="left:1121px;top:3069px;background:#fff;border:1px solid #ddd"><svg width="10" height="14"><path d="M2 1L8 7L2 13" fill="none" stroke="#333" stroke-width="1.6"/></svg></div>
</section>

<footer>
  <div class="abs footer">
    <div class="social-dots"><span></span><span></span><span></span><span></span></div>
  </div>
  <div class="abs f-brand">Brisk Meadow</div>
  <div class="abs f-col" style="left:352px"><h4>Company</h4><ul><li>Our Story</li><li>Careers</li><li>Privacy Policy</li><li>Terms and Conditions</li></ul></div>
  <div class="abs f-col" style="left:592px"><h4>Help</h4><ul><li>Returns &amp; Exchanges</li><li>FAQ</li><li>Size Guide</li><li>Search</li></ul></div>
  <div class="abs f-col" style="left:815px"><h4>Newsletter</h4><p>Lorem ipsum dolor sit amet, consectetur adipi scing elit, sed do eiusmod tempor</p></div>
  <div class="abs email">Email address
    <svg style="position:absolute;right:16px;top:15px" width="16" height="16" viewBox="0 0 16 16"><path d="M1 8L15 1L11 15L8 9Z" fill="var(--teal)"/></svg>
  </div>
  <div class="abs copy">© Copyrights Company name 2021. All rights reserved | Privacy policy | Terms Condition</div>
</footer>

<div class="abs chat"><svg width="28" height="24" viewBox="0 0 28 24"><path d="M14 2C7 2 2 6 2 11c0 3 2 5 4 6l-1 5 6-3c1 0 2 .3 3 .3 7 0 12-4 12-9S21 2 14 2Z" fill="#fff"/></svg></div>

</body>
</html>
```